Dolsemk Business Cards

Business cards for real estate
Target Market(s)
Real estate
Industry/Entity Type
Real Estate Agent
Font styles to use
Serif
Requirements
Must have
- Photo and logo

```html
<!DOCTYPE html>
<html lang="en">
<head>
<meta charset="utf-8">
<title>Dolsemk Realty Business Card</title>
<link rel="stylesheet" href="https://fonts.googleapis.com/css2?family=Playfair+Display:wght@400;500&family=Roboto:wght@400;500&display=swap">
<style>
  :root {
    --canvas: #2b2824;
    --card: #0d0d0e;
    --card-edge: #1c1c1e;
    --gold: #d9b77a;
    --gold-dark: #a8874f;
    --ink: #f2f2f2;
    --ink-soft: #cfcfcf;
    --mark: #b0303a;
    --photo-a: #3a3d48;
    --photo-b: #6a6d78;
  }
  * { box-sizing: border-box; margin: 0; padding: 0; }
  html, body { width: 1200px; height: 1022px; overflow: hidden; }
  body {
    background: var(--canvas);
    display: flex; align-items: center; justify-content: center;
    font-family: "Roboto", Arial, sans-serif;
  }
  .business-card {
    position: relative;
    width: 900px; height: 514px;
    background: linear-gradient(180deg, var(--card-edge) 0%, var(--card) 55%);
    border-radius: 26px;
    overflow: hidden;
    display: flex;
    box-shadow: 0 20px 50px rgba(0,0,0,.45);
  }
  .agent-photo {
    width: 420px; height: 100%;
    background: linear-gradient(160deg, var(--photo-b) 0%, var(--photo-a) 60%, var(--card) 100%);
  }
  .card-details {
    flex: 1;
    position: relative;
    padding: 56px 70px 50px 40px;
    color: var(--ink);
  }
  .brand {
    display: flex; align-items: center; gap: 20px;
  }
  .brand-dot {
    width: 64px; height: 64px; border-radius: 50%;
    background: var(--mark);
  }
  .brand-name {
    font-family: "Playfair Display", Georgia, serif;
    font-weight: 400;
    font-size: 44px;
    line-height: 1.02;
    letter-spacing: 2px;
    color: var(--ink);
  }
  .brand-name span { display: block; letter-spacing: 9px; }
  .agent-name {
    margin-top: 46px;
    font-weight: 500;
    font-size: 30px;
    letter-spacing: 1px;
    color: var(--gold);
    text-transform: uppercase;
  }
  .agent-role {
    margin-top: 6px;
    font-size: 20px;
    color: var(--ink-soft);
  }
  .contact-list {
    list-style: none;
    margin-top: 28px;
    font-size: 19px;
    line-height: 1.6;
    color: var(--ink);
  }
  .contact-list li { display: flex; align-items: center; justify-content: space-between; }
  .contact-list svg { width: 16px; height: 16px; fill: none; stroke: var(--gold); stroke-width: 2; }
  .gold-tab {
    position: absolute; top: 0; right: 70px;
    width: 44px; height: 18px;
    background: linear-gradient(90deg, var(--gold-dark), var(--gold), var(--gold-dark));
  }
</style>
</head>
<body>
  <div class="business-card">
    <div class="agent-photo" role="img" aria-label="Portrait photo of the agent in a dark pinstripe suit and light blue tie"></div>
    <div class="card-details">
      <div class="gold-tab"></div>
      <div class="brand">
        <div class="brand-dot"></div>
        <div class="brand-name">DOLSEMK<span>REALTY</span></div>
      </div>
      <p class="agent-name">Callum Reeve</p>
      <p class="agent-role">Director</p>
      <ul class="contact-list">
        <li>52b Harlow Street,<span></span></li>
        <li>Lindenvale, NZ, 8042<span></span></li>
        <li>(514) 555-0187
          <svg viewBox="0 0 16 16"><path d="M4 2 L6 5 L5 7 Q7 10 9 11 L11 10 L14 12 L13 14 Q6 14 2 4 Z"/></svg></li>
        <li>info@dolsemkrealty.com
          <svg viewBox="0 0 16 16"><rect x="2" y="4" width="12" height="9"/><path d="M2 4 L8 9 L14 4"/></svg></li>
        <li>www.dolsemkrealty.com
          <svg viewBox="0 0 16 16"><circle cx="8" cy="8" r="6"/><path d="M2 8 H14 M8 2 Q4 8 8 14 Q12 8 8 2"/></svg></li>
      </ul>
    </div>
  </div>
</body>
</html>
```